Postcard Design Project

I am an answering service and appointment scheduler for various Real Estate Appraisers around the country. This is for soliciting new clients.

Industry/Entity Type

Real Estate

```html
<!DOCTYPE html>
<html lang="en">
<head>
<meta charset="utf-8">
<title>Attention Appraisers – Postcard</title>
<link href="https://fonts.googleapis.com/css2?family=Fira+Sans+Extra+Condensed:wght@400;600;700&family=Open+Sans:wght@400;700;800&display=swap" rel="stylesheet">
<style>
  :root{
    --page:#e9e9e9;
    --card:#ffffff;
    --ink:#111111;
    --panel:#f3f5fa;
    --blue:#2a8fd6;
    --blue-deep:#1a6fb4;
    --blue-light:#4fb8e6;
    --sky-top:#2d6fc6;
    --sky-mid:#8fbbe9;
    --white:#ffffff;
    --social-dark:#2c4f8f;
  }
  *{margin:0;padding:0;box-sizing:border-box;}
  html,body{width:1200px;height:1200px;overflow:hidden;background:var(--page);}
  body{position:relative;font-family:"Fira Sans Extra Condensed",sans-serif;color:var(--ink);}

  .postcard{position:absolute;left:30px;top:187px;width:1141px;height:826px;background:var(--card);box-shadow:0 4px 14px rgba(0,0,0,.18);}
  .frame{position:absolute;left:23px;top:23px;width:1095px;height:780px;overflow:hidden;background:var(--panel);}

  .headline{position:absolute;left:0;top:0;width:100%;height:67px;background:var(--ink);color:var(--white);
    font-weight:700;font-size:50px;line-height:67px;text-align:center;letter-spacing:.3px;}
  .rule{position:absolute;left:0;top:73px;width:100%;height:5px;background:var(--blue);}

  .hero-photo{position:absolute;left:0;top:79px;width:547px;height:620px;
    background:radial-gradient(circle at 70% 45%, #ffffff 0%, #d8e8f8 22%, var(--sky-mid) 48%, var(--sky-top) 100%);}

  .services{position:absolute;left:600px;top:103px;width:330px;font-size:22px;line-height:31px;}
  .services h2{font-weight:400;font-size:22px;}
  .services ul{list-style:none;}
  .services li{position:relative;padding-left:26px;white-space:nowrap;}
  .services li::before{content:"";position:absolute;left:3px;top:8px;border-left:13px solid var(--blue-deep);
    border-top:8px solid transparent;border-bottom:8px solid transparent;}

  .price-badge{position:absolute;left:902px;top:92px;width:160px;height:160px;border-radius:50%;
    background:var(--white);box-shadow:0 2px 6px rgba(0,0,0,.25);}
  .price-badge .disc{position:absolute;inset:8px;border-radius:50%;
    background:radial-gradient(circle at 40% 30%, var(--blue-light), var(--blue-deep));
    color:var(--white);text-align:center;}
  .price-badge .amount{display:block;font-weight:600;font-size:50px;line-height:50px;margin-top:30px;}
  .price-badge .unit{display:block;font-size:20px;line-height:22px;}

  .offer{position:absolute;left:569px;top:416px;width:500px;text-align:center;font-weight:600;font-size:23px;line-height:32px;white-space:nowrap;}

  .brand{position:absolute;left:583px;top:566px;width:500px;text-align:center;white-space:nowrap;
    font-weight:600;font-size:38px;line-height:44px;color:var(--blue-deep);letter-spacing:1px;}
  .brand .mark{display:inline-block;width:16px;height:16px;background:var(--blue-deep);margin-right:10px;vertical-align:middle;}

  .social{position:absolute;top:624px;width:39px;height:39px;border-radius:50%;}
  .social.one{left:987px;background:var(--social-dark);}
  .social.two{left:1035px;background:var(--blue-light);}

  .footer-band{position:absolute;left:0;top:630px;width:1095px;height:150px;}

  .tagline{position:absolute;left:0;top:686px;width:100%;text-align:center;color:var(--white);font-weight:600;font-size:28px;line-height:34px;}
  .call{position:absolute;left:0;top:718px;width:100%;height:52px;text-align:center;color:var(--white);font-family:"Open Sans",sans-serif;line-height:52px;white-space:nowrap;}
  .call .lead{font-size:25px;}
  .call .number{font-weight:800;font-size:46px;letter-spacing:.5px;}
</style>
</head>
<body>
  <div class="postcard">
    <div class="frame">
      <h1 class="headline">ATTENTION APPRAISERS!!!</h1>
      <div class="rule"></div>

      <div class="hero-photo" role="img" aria-label="Photo of a hand holding a small white house with a red roof against a bright blue sky with clouds"></div>

      <section class="services">
        <h2>What we do for you:</h2>
        <ul>
          <li>Answer all of your phone calls.</li>
          <li>Set-up all of your appointments.</li>
          <li>Answer all of your e-mail.</li>
          <li>Update AMC's and Clients.</li>
          <li>Update licenses and E&amp;O.</li>
          <li>Prep your reports with pertinent data.</li>
          <li>Provide plat maps, zoning, field cards &amp;<br>MLS sheets to your work file.</li>
        </ul>
      </section>

      <div class="price-badge">
        <div class="disc">
          <span class="amount">$67</span>
          <span class="unit">PER ORDER</span>
        </div>
      </div>

      <p class="offer">All for the low introductory price of $67 per order.<br>Regularly $79 a 15% savings!!!</p>

      <div class="brand"><span class="mark"></span>THE VALUATION DESK</div>

      <span class="social one"></span>
      <span class="social two"></span>

      <svg class="footer-band" viewBox="0 0 1095 150" aria-hidden="true">
        <polygon points="0,52 548,8 1095,52 1095,150 0,150" fill="#1d1d1d"/>
        <polygon points="0,61 548,17 1095,61 1095,150 0,150" fill="#ffffff"/>
        <polygon points="0,65 548,21 1095,65 1095,150 0,150" fill="#2a8fd6"/>
      </svg>

      <p class="tagline">We Take Care of the Office so you can...Well…Appraise!</p>
      <p class="call"><span class="lead">Call today!!! </span><span class="number">401-555-0142</span></p>
    </div>
  </div>
</body>
</html>
```